photowall advertisement

We require a wall featuring our company logo. We would like to avoid the color green, and gold is highly preferred. The design should be similar to the one in the attached photo. The wall will be used for photos and promotional purposes during congresses. Files must be prepared for printing.
dimension of wall: 470x223 cm

Industry/Entity Type

lifestyle

Colors
0054AA
0677BA
7BADD7
CADEEF
E8F1F8
6B429C
8869AF
B7A5CE
E3DAEB
F3F0F8

Requirements
Must have
• gold color, white, and other compare with gold color
Nice to have
• some pictograms, maps of Europe

```html
<!DOCTYPE html>
<html lang="en">
<head>
<meta charset="utf-8">
<title>Nova Line Studio – Photo Wall</title>
<link rel="stylesheet" href="https://fonts.googleapis.com/css2?family=Saira+Condensed:wght@600;700&display=swap">
<style>
  :root {
    --page: #d3d3d3;
    --navy: #0c1120;
    --navy-soft: #1b2336;
    --white: #ffffff;
    --gold-deep: #b4893a;
    --gold-light: #ecdc8c;
    --gold-line: #b08a3e;
    --ink: #111522;
  }
  * { box-sizing: border-box; margin: 0; padding: 0; }
  html, body {
    width: 910px; height: 1200px; overflow: hidden;
    background: var(--page);
  }
  .backdrop {
    position: absolute;
    left: 40px; top: 403px;
    width: 830px; height: 394px;
    overflow: hidden;
    background:
      radial-gradient(ellipse 60% 55% at 50% 50%, var(--navy-soft), transparent 75%),
      var(--navy);
    font-family: "Saira Condensed", sans-serif;
    font-weight: 700;
  }
  .backdrop__lines {
    position: absolute; inset: 0;
    width: 100%; height: 100%;
  }
  .row {
    position: absolute; left: 37px;
    display: grid;
    grid-template-columns: repeat(4, 178px);
    column-gap: 15px;
  }
  .row--brand { height: 26px; }
  .row--brand-1 { top: 28px; }
  .row--brand-2 { top: 114px; }
  .row--brand-3 { top: 201px; }
  .row--cards { height: 37px; }
  .row--cards-1 { top: 67px; }
  .row--cards-2 { top: 154px; }
  .row--cards-3 { top: 241px; }

  .brand {
    display: flex; align-items: center; gap: 8px;
    color: var(--white);
    font-size: 22px; letter-spacing: 1px;
    line-height: 1; text-transform: uppercase;
    white-space: nowrap;
  }
  .brand__square {
    width: 14px; height: 14px; background: var(--gold-light);
    flex: none;
  }

  .card-pair { display: grid; gap: 14px; height: 37px; }
  .card-pair--wide-first { grid-template-columns: 102px 62px; }
  .card-pair--small-first { grid-template-columns: 62px 102px; }
  .card {
    background: var(--white);
    border-radius: 3px;
    display: flex; align-items: center; justify-content: center;
    color: var(--ink);
    text-transform: uppercase; text-align: center;
    line-height: 1;
  }
  .card--wide { font-size: 12px; letter-spacing: .5px; }
  .card--small { font-size: 10px; letter-spacing: .3px; }

  .url-band {
    position: absolute; left: 0; right: 0;
    top: 298px; height: 23px;
    background: linear-gradient(90deg, var(--gold-deep), #d9c070 25%, var(--gold-light) 50%, #d9c070 75%, var(--gold-deep));
    display: flex; justify-content: space-between; align-items: center;
    padding: 0 37px 0 37px;
  }
  .url-band__link {
    color: var(--ink);
    font-size: 15px; font-weight: 600; letter-spacing: .2px;
    text-decoration: none;
  }
</style>
</head>
<body>
<main class="backdrop" aria-label="Nova Line Studio photo wall">
  <svg class="backdrop__lines" viewBox="0 0 830 394" aria-hidden="true">
    <g stroke="var(--gold-line)" stroke-width="0.8" fill="none" opacity="0.8">
      <line x1="0" y1="48" x2="80" y2="0"/>
      <line x1="128" y1="0" x2="205" y2="55"/>
      <line x1="97" y1="0" x2="78" y2="38"/>
      <line x1="715" y1="0" x2="800" y2="26"/>
      <line x1="830" y1="70" x2="760" y2="18"/>
      <line x1="15" y1="394" x2="175" y2="322"/>
      <line x1="395" y1="325" x2="440" y2="394"/>
      <line x1="520" y1="394" x2="760" y2="322"/>
      <line x1="745" y1="394" x2="778" y2="322"/>
    </g>
  </svg>

  <div class="row row--brand row--brand-1">
    <div class="brand"><span class="brand__square"></span>Nova Line Studio</div>
    <div class="brand"><span class="brand__square"></span>Nova Line Studio</div>
    <div class="brand"><span class="brand__square"></span>Nova Line Studio</div>
    <div class="brand"><span class="brand__square"></span>Nova Line Studio</div>
  </div>
  <div class="row row--cards row--cards-1">
    <div class="card-pair card-pair--wide-first"><div class="card card--wide">Nova Line Studio</div><div class="card card--small">Nova Line<br>Studio</div></div>
    <div class="card-pair card-pair--wide-first"><div class="card card--wide">Nova Line Studio</div><div class="card card--small">Nova Line<br>Studio</div></div>
    <div class="card-pair card-pair--wide-first"><div class="card card--wide">Nova Line Studio</div><div class="card card--small">Nova Line<br>Studio</div></div>
    <div class="card-pair card-pair--wide-first"><div class="card card--wide">Nova Line Studio</div><div class="card card--small">Nova Line<br>Studio</div></div>
  </div>

  <div class="row row--brand row--brand-2">
    <div class="brand"><span class="brand__square"></span>Nova Line Studio</div>
    <div class="brand"><span class="brand__square"></span>Nova Line Studio</div>
    <div class="brand"><span class="brand__square"></span>Nova Line Studio</div>
    <div class="brand"><span class="brand__square"></span>Nova Line Studio</div>
  </div>
  <div class="row row--cards row--cards-2">
    <div class="card-pair card-pair--small-first"><div class="card card--small">Nova Line<br>Studio</div><div class="card card--wide">Nova Line Studio</div></div>
    <div class="card-pair card-pair--small-first"><div class="card card--small">Nova Line<br>Studio</div><div class="card card--wide">Nova Line Studio</div></div>
    <div class="card-pair card-pair--small-first"><div class="card card--small">Nova Line<br>Studio</div><div class="card card--wide">Nova Line Studio</div></div>
    <div class="card-pair card-pair--small-first"><div class="card card--small">Nova Line<br>Studio</div><div class="card card--wide">Nova Line Studio</div></div>
  </div>

  <div class="row row--brand row--brand-3">
    <div class="brand"><span class="brand__square"></span>Nova Line Studio</div>
    <div class="brand"><span class="brand__square"></span>Nova Line Studio</div>
    <div class="brand"><span class="brand__square"></span>Nova Line Studio</div>
    <div class="brand"><span class="brand__square"></span>Nova Line Studio</div>
  </div>
  <div class="row row--cards row--cards-3">
    <div class="card-pair card-pair--wide-first"><div class="card card--wide">Nova Line Studio</div><div class="card card--small">Nova Line<br>Studio</div></div>
    <div class="card-pair card-pair--wide-first"><div class="card card--wide">Nova Line Studio</div><div class="card card--small">Nova Line<br>Studio</div></div>
    <div class="card-pair card-pair--wide-first"><div class="card card--wide">Nova Line Studio</div><div class="card card--small">Nova Line<br>Studio</div></div>
    <div class="card-pair card-pair--wide-first"><div class="card card--wide">Nova Line Studio</div><div class="card card--small">Nova Line<br>Studio</div></div>
  </div>

  <div class="url-band">
    <span class="url-band__link">www.novalinestudio.com</span>
    <span class="url-band__link">www.novalinestudio.com</span>
    <span class="url-band__link">www.novalinestudio.com</span>
  </div>
</main>
</body>
</html>
```